Flyer for Compassion training days

I need a A5-size, single-sided flyer design for my training days. They are weekends in a blend of Compassionate Communication and Buddhist teachings called Palomere Communication. The logo for Palomere that should be included.
The flyer needs room for 1) course title, 2) course dates, location & price, 3) course description, 4) booking info, 5) my picture & short bio, and 6) the palomere.co website (yes, it is 'co' and not 'com).
Updates

Target Market(s)

Women 35-65 years, well-educated, spiritually minded. May have interests like yoga and meditation.

Industry/Entity Type

Health And Wellness

Font styles to use
Sans Serif
Other font styles liked:
• Blue Plaque, Josefina are both great

Colors
fbf289
fdf9cf
cfeae6
33b8a4

Requirements
Must have
• The Palomere logo; my picture.
• Elegance. Calm and expansive feel.
• The poster provided in the project files shows you the kind of information I need to include.
• Colours -- greens and yellows, but the options on pixel harbor are not quite the right shades.
• The logo colour can be changed.
Nice to have
• Classy (but not cliche) image associated with Buddhism; gentle curves similar to those on the business card (see project files).
Should not have
• Dark background. Busy, loud design. Overly 'swirly' design. Images that I have to buy separately.

```html
<!DOCTYPE html>
<html lang="en">
<head>
<meta charset="utf-8">
<title>Palomere Communication – Core Course Flyer</title>
<link rel="stylesheet" href="https://fonts.googleapis.com/css2?family=Josefin+Sans:wght@400;600;700&family=Ubuntu:wght@500;700&display=swap">
<style>
  :root {
    --page-bg: #e9ebe6;
    --paper: #f7f7f6;
    --ink: #2f2f2f;
    --ink-dark: #3b3b3d;
    --navy: #3d4a6b;
    --teal: #1e9e88;
    --teal-soft: #33b8a4;
    --photo-warm: #d8c9b8;
    --photo-stone: #7b7f80;
  }
  * { box-sizing: border-box; margin: 0; padding: 0; }
  html, body { width: 1200px; height: 1199px; overflow: hidden; background: var(--page-bg); }
  body { position: relative; font-family: "Josefin Sans", sans-serif; color: var(--ink); }

  .flyer {
    position: absolute; left: 328px; top: 55px; width: 760px; height: 1078px;
    background: radial-gradient(ellipse at 40% 40%, #ffffff 0%, var(--paper) 60%, #ecebea 100%);
    overflow: hidden;
  }
  .photo-column {
    position: absolute; left: 565px; top: 0; width: 195px; height: 880px;
    background: linear-gradient(180deg, #efe3d6 0%, var(--photo-warm) 35%, #b9b3ab 60%, var(--photo-stone) 100%);
  }
  .ribbon-area {
    position: absolute; left: 565px; top: 0; width: 195px; height: 160px;
    background: linear-gradient(160deg, rgba(51,184,164,0.35), rgba(59,59,61,0.2));
  }
  .curves { position: absolute; inset: 0; }

  .equation {
    position: absolute; left: 87px; top: 38px;
    font-weight: 700; font-size: 26px; line-height: 29px; color: var(--navy);
  }
  .title {
    position: absolute; left: 85px; top: 112px;
    font-family: "Ubuntu", sans-serif; font-weight: 700; font-size: 62px; line-height: 56px;
    color: var(--ink-dark); letter-spacing: -0.5px;
  }
  .badge {
    position: absolute; color: #fff;
    border-radius: 0 14px 0 14px; display: flex; align-items: center; justify-content: center;
  }
  .badge--course { left: 82px; top: 241px; width: 210px; height: 51px; background: var(--ink-dark); font-size: 29px; font-weight: 600; padding-top: 4px; }
  .badge--booking { left: 76px; top: 832px; width: 124px; height: 33px; background: var(--teal); font-size: 23px; font-weight: 600; padding-top: 3px; }
  .badge--facilitator { left: 76px; top: 888px; width: 124px; height: 32px; background: var(--ink-dark); font-size: 22px; font-weight: 600; padding-top: 3px; }

  .website { position: absolute; left: 344px; top: 258px; font-size: 23px; font-weight: 600; color: var(--ink); }

  .brand-mark {
    position: absolute; left: 44px; top: 360px; display: flex; align-items: center; gap: 8px;
    font-weight: 700; font-size: 26px; color: var(--teal-soft);
  }
  .brand-mark__dot { width: 22px; height: 22px; border-radius: 50%; background: var(--teal-soft); }

  .intro { position: absolute; left: 220px; top: 321px; width: 335px; font-size: 18px; line-height: 23.5px; letter-spacing: -0.2px; }
  .explore-heading { position: absolute; left: 79px; top: 485px; font-size: 24px; font-weight: 600; color: var(--teal); }

  .topics { position: absolute; left: 86px; top: 537px; width: 470px; list-style: none; font-size: 18.5px; line-height: 22px; }
  .topics li { position: relative; margin-bottom: 6px; }
  .topics li::before { content: ""; position: absolute; left: -17px; top: 7px; width: 6px; height: 6px; border-radius: 50%; background: var(--ink); }

  .audience { position: absolute; left: 86px; top: 703px; width: 455px; font-size: 17.5px; line-height: 21.8px; }

  .booking-info { position: absolute; left: 219px; top: 832px; font-size: 20px; font-weight: 700; line-height: 26px; color: var(--ink); }
  .booking-info .email { color: var(--teal); }

  .bio { position: absolute; left: 86px; top: 907px; width: 445px; font-size: 17.5px; line-height: 22px; text-indent: 142px; }
  .coaching { position: absolute; left: 88px; top: 1011px; font-size: 18px; font-weight: 700; white-space: nowrap; }

  .event-details {
    position: absolute; left: 580px; top: 166px; font-size: 20px; font-weight: 700; line-height: 24px;
    color: #2a2a2a; letter-spacing: -0.3px; white-space: nowrap;
  }
  .event-details p { margin-bottom: 11px; }

  .portrait {
    position: absolute; left: 553px; top: 868px; width: 170px; height: 170px; border-radius: 50%;
    border: 4px solid var(--ink-dark);
    background: radial-gradient(circle at 50% 40%, #a89a88 0%, #6d6254 60%, #3e3730 100%);
  }
</style>
</head>
<body>
  <main class="flyer">
    <div class="photo-column" role="img" aria-label="Photograph of a stone Buddha head in soft, warm bokeh light"></div>
    <div class="ribbon-area" role="img" aria-label="Decorative teal and charcoal ribbon ornament"></div>

    <svg class="curves" width="760" height="1078" viewBox="0 0 760 1078" aria-hidden="true">
      <path d="M565 730 C565 800 600 815 640 830 C690 848 740 838 760 840 L760 1078 L565 1078 Z" fill="#f4f3f2"/>
      <line x1="565" y1="0" x2="565" y2="740" stroke="#ffffff" stroke-width="8"/>
      <line x1="570" y1="298" x2="760" y2="298" stroke="var(--ink-dark)" stroke-width="4"/>
      <path d="M0 385 C20 430 30 470 52 510 C60 522 70 524 90 524 L562 524" fill="none" stroke="var(--teal)" stroke-width="3"/>
      <path d="M562 682 L110 682 C70 682 55 700 45 740 C35 780 20 805 0 812" fill="none" stroke="var(--teal)" stroke-width="3"/>
      <path d="M565 730 C555 790 545 830 510 870 C480 890 440 892 400 892 L210 892" fill="none" stroke="var(--ink-dark)" stroke-width="3"/>
      <path d="M565 740 C570 800 600 815 640 830 C690 848 740 838 760 840" fill="none" stroke="var(--ink-dark)" stroke-width="3"/>
    </svg>

    <p class="equation">Mindfullness + Kindness +<br>Compassionate Communication =</p>
    <h1 class="title">Palomere<br>Communication</h1>
    <div class="badge badge--course">Core Course</div>
    <p class="website">www.palomere.co</p>

    <div class="brand-mark"><span class="brand-mark__dot"></span>Palomere</div>

    <p class="intro">Palomere Communication can help you increase awareness &amp; compassion in everyday speech (with yourself &amp; others), better understand your own patterns, and build resilience to challenging situations. Choose from:</p>

    <h2 class="explore-heading">In this 2-day Core Course, we’ll explore:</h2>
    <ul class="topics">
      <li>Compassionate Communication;</li>
      <li>Buddhist teachings on Right Speech, loving-kindness, Right Effort, and more;</li>
      <li>mindfulness practices;</li>
      <li>choices available to us in our everyday speech.</li>
    </ul>

    <p class="audience">This workshop will be of interest if you’d like to improve personal and/or professional relationships.&nbsp; Open to all, best suited to those with at least 1 year’s experience with Mindfulness,&nbsp; Buddhism, or Compassionate Communication / NVC.</p>

    <div class="badge badge--booking">booking</div>
    <p class="booking-info">Book online at Ticketvale or<br>write <span class="email">maribel@palomere.co</span></p>

    <div class="badge badge--facilitator">facilitator</div>
    <p class="bio">Maribel Ostrander is an experienced group facilitator, having worked with a range of organisations and presented at a number of festivals &amp; conferences.</p>
    <p class="coaching">Maribel offers coaching in Palomere Communication.</p>

    <div class="event-details">
      <p>11-12 Dec</p>
      <p>Elmgate Centre,<br>Edinburgh</p>
      <p>£125/100</p>
    </div>

    <div class="portrait" role="img" aria-label="Portrait photograph of the facilitator, Maribel Ostrander"></div>
  </main>
</body>
</html>
```